I am a company selling interior designing materials

HI, I am selling interior design materials and require a namecard which is more outstanding while following a certain details placement as attached.

My clients are mainly interior designers so it has to attract their attention rather than feeling that its "just another namecard". I am selling wallcoverings, fabrics, acoustics and carpets.

Target Market(s)

interior designers designing hotels, commerical offices.

Contact Information for Business Card

As per attached.
Please change address to 47 Jalan 16 Tampines #05-02 Velmora Building Singapore 527314

Font styles to use
Other font styles liked:
• calibri

Requirements
Must have
• (1) company logo on top in the middle. Placement of contac details to be the same
• (2) company color is blue/green cymk 75/8/42/0
• (3) "KTV" logo to be prominent
• (4) You may change the logo but there should be a "swirl" surrounding the word KTV like current logo. The swirl pattern does not need to follow current logo and you may propose.
Should not have
• (1) there should not be any designs above "KTV" logo
• (2) no sharp triangles or angles

```html
<!DOCTYPE html>
<html lang="en">
<head>
<meta charset="utf-8">
<title>KaiTeVa Interior Furnishings – Name Card</title>
<link rel="stylesheet" href="https://fonts.googleapis.com/css2?family=Ubuntu:wght@500;700&family=Roboto:wght@400&display=swap">
<style>
  :root {
    --teal: #00918a;
    --teal-deep: #00857c;
    --red: #c4261d;
    --ink: #3f4750;
    --text: #444a4f;
    --card-white: #f4f4f4;
    --backdrop: #e4e4e4;
  }
  * { margin: 0; padding: 0; box-sizing: border-box; }
  html, body {
    width: 1200px; height: 576px; overflow: hidden;
    background: var(--backdrop);
  }
  .canvas { position: relative; width: 1200px; height: 576px; }

  .card {
    position: absolute; top: 139px;
    width: 484px; height: 292px;
    border-radius: 13px; overflow: hidden;
  }

  /* Front */
  .card-front {
    left: 82px;
    background: linear-gradient(180deg, var(--teal) 0%, var(--teal-deep) 100%);
  }
  .front-mark {
    position: absolute; left: 0; right: 0; top: 118px;
    text-align: center;
    font-family: "Ubuntu", sans-serif; font-weight: 700;
    font-size: 52px; line-height: 56px; letter-spacing: 1px;
    color: #ffffff;
  }

  /* Back */
  .card-back {
    left: 602px;
    background: var(--card-white);
    font-family: "Roboto", sans-serif; color: var(--text);
  }
  .edge-tab {
    position: absolute; left: -20px; top: 43px;
    width: 28px; height: 48px; border-radius: 50%;
    background: var(--teal);
  }
  .holder { position: absolute; left: 30px; top: 48px; }
  .holder-name {
    font-family: "Ubuntu", sans-serif; font-weight: 500;
    font-size: 20px; line-height: 24px; color: var(--teal);
  }
  .holder-mobile { font-size: 12px; line-height: 16px; margin-top: 2px; }

  .brand {
    position: absolute; left: 250px; width: 200px; top: 46px;
    text-align: center; color: var(--ink);
  }
  .brand-mark {
    font-family: "Ubuntu", sans-serif; font-weight: 700;
    font-size: 38px; line-height: 42px; letter-spacing: 1px;
  }
  .brand-name {
    margin-top: 8px;
    font-family: "Ubuntu", sans-serif; font-weight: 700;
    font-size: 17.5px; line-height: 20px; white-space: nowrap;
  }
  .brand-legal {
    display: flex; align-items: center; gap: 6px; justify-content: center;
    font-family: "Ubuntu", sans-serif; font-weight: 700;
    font-size: 10.5px; line-height: 14px; margin-top: 1px;
  }
  .brand-legal::before, .brand-legal::after {
    content: ""; width: 30px; height: 1.5px; background: var(--teal);
  }

  .contacts { position: absolute; left: 28px; top: 160px; font-size: 12px; }
  .contact-row { display: flex; align-items: center; height: 17px; }
  .contact-row svg { width: 11px; height: 11px; margin: 0 12px 0 6px; fill: var(--teal); }
  .address { margin-top: 6px; line-height: 19px; }

  .swoosh { position: absolute; left: 0; bottom: 0; width: 484px; height: 292px; }
</style>
</head>
<body>
<main class="canvas">

  <section class="card card-front" aria-label="Card front">
    <div class="front-mark">KTV</div>
  </section>

  <section class="card card-back" aria-label="Card back">
    <div class="edge-tab"></div>

    <div class="holder">
      <p class="holder-name">Lena Ong</p>
      <p class="holder-mobile">(65) 9127 4406</p>
    </div>

    <div class="brand">
      <p class="brand-mark">KTV</p>
      <p class="brand-name">KaiTeVa Interior</p>
      <p class="brand-legal">Furnishings Pte Ltd</p>
    </div>

    <div class="contacts">
      <p class="contact-row">
        <svg viewBox="0 0 12 12" aria-hidden="true"><path d="M1 4.5C1 2.5 3.5 1.5 6 1.5s5 1 5 3L9 5.2 8.3 3.8H3.7L3 5.2z M2.5 6.5h7l1 4h-9z"/></svg>
        (65) 6382 1175
      </p>
      <p class="contact-row">
        <svg viewBox="0 0 12 12" aria-hidden="true"><path d="M1 2.5h10v7H1z M1.6 3.1 6 6.6l4.4-3.5" fill="none" stroke="#00918a" stroke-width="1.4"/></svg>
        lena@ktvfurnishings.com
      </p>
      <p class="contact-row">
        <svg viewBox="0 0 12 12" aria-hidden="true"><circle cx="6" cy="6" r="5"/><path d="M1 6h10M6 1c-2 2.5-2 7.5 0 10M6 1c2 2.5 2 7.5 0 10" fill="none" stroke="#f4f4f4" stroke-width="0.9"/></svg>
        www.ktvfurnishings.com
      </p>
      <p class="address">47 Jalan 16 Tampines #05-02<br>Velmora Building Singapore 527314</p>
    </div>

    <svg class="swoosh" viewBox="0 0 484 292" aria-hidden="true">
      <path d="M0 267 Q170 280 340 292 L0 292 Z" fill="var(--red)"/>
      <path d="M120 292 Q380 290 484 253 L484 292 Z" fill="var(--teal)"/>
    </svg>
  </section>

</main>
</body>
</html>
```